wooden jewelry - pearl necklaces

I sell wooden jeweler (rings and pearls) on markets, and so on. I also opened my business as a carpenter. The rings and a combination of wood and metal. The wood is special wood, not very common on Europe. I paint the rings afterwards. You can see some of the pictures on the pictures I uploaded. The pearls are made of the same kind of wood and colored in all kinds of colors. They are then assembled to bracelets. The jewelry is very individual and looks really cool and all kinds of people.

Target Market(s)

Young urban alternative with a sense of individuality

Contact Information for Business Card

Front:

Text:

„Kugelwerk“ (big)
„Malte Oswitz“ (smaler)

Back
„Holzschmuck
Herstellung von individuellem Holz- und Modeschmuck

Malte Oswitz
Tel: 015239460518
Lindgarbweg 9
83127 Burghausen

malteoswitz@postfeld.de“

Font styles to use
Sans Serif

Requirements
Nice to have
• Nice to see a camel thorn tree on the background, this is a special wood and some of the rings are made out of this wood.

```html
<!DOCTYPE html>
<html lang="de">
<head>
<meta charset="utf-8">
<title>Kugelwerk – Visitenkarte</title>
<link rel="stylesheet" href="https://fonts.googleapis.com/css2?family=Arimo:wght@700&display=swap">
<style>
  :root {
    --card-bg: #ffffff;
    --brand-brown: #4a1915;
    --name-plum: #8b4e7b;
    --backdrop-grey: #e4e4e4;
    --bead-dark: #3a1a14;
    --bead-mid: #9a5a32;
    --bead-light: #e6c98f;
    --bead-red: #b8323f;
  }
  html, body {
    margin: 0;
    padding: 0;
    width: 1200px;
    height: 720px;
    overflow: hidden;
    background: var(--card-bg);
  }
  .card-front {
    position: relative;
    width: 1200px;
    height: 720px;
    background: var(--card-bg);
    overflow: hidden;
    font-family: "Arimo", Arial, Helvetica, sans-serif;
  }
  .bead-photo {
    position: absolute;
    left: 0;
    top: 0;
    width: 435px;
    height: 720px;
    background:
      radial-gradient(circle at 30% 25%, var(--bead-light) 0%, transparent 45%),
      radial-gradient(circle at 75% 70%, var(--bead-red) 0%, transparent 35%),
      radial-gradient(circle at 60% 40%, var(--bead-mid) 0%, transparent 55%),
      linear-gradient(160deg, var(--bead-mid), var(--bead-dark) 55%, var(--bead-mid));
  }
  .tree-backdrop {
    position: absolute;
    left: 435px;
    top: 0;
    width: 765px;
    height: 720px;
    background: linear-gradient(to bottom, var(--backdrop-grey) 0%, #f2f2f2 55%, var(--card-bg) 100%);
  }
  .brand {
    position: absolute;
    left: 460px;
    width: 690px;
    text-align: center;
    margin: 0;
    font-weight: 700;
    white-space: nowrap;
  }
  .brand-name {
    top: 236px;
    font-size: 114px;
    line-height: 1;
    color: var(--brand-brown);
    letter-spacing: -1px;
  }
  .owner-name {
    top: 358px;
    font-size: 38px;
    line-height: 1;
    color: var(--name-plum);
  }
</style>
</head>
<body>
  <main class="card-front">
    <div class="bead-photo" role="img" aria-label="Foto vieler bunter Holzperlen in Braun-, Natur-, Schwarz- und Rottönen"></div>
    <div class="tree-backdrop" role="img" aria-label="Hellgraue Silhouette eines Kameldornbaums im Hintergrund"></div>
    <h1 class="brand brand-name">Kugelwerk</h1>
    <p class="brand owner-name">Malte Oswitz</p>
  </main>
</body>
</html>
```